"Eyebrow Threading Flyer Design"

We need a flyer design for a new service that will be provided in our established Beauty Salon in Toorak called "Threading". We provide all beauty services for our clients & would like to now introduce this very popular ancient method of hair removal.
Following are four "40% Off Threading Combo Packages" that will hopefully tempt new clients into our salon.
#Package 1- Eyebrow Threading plus Eyebrow Tint or Eyelash Tint Normally $53 Now $32
#Package 2- Eyebrow Threading plus Full Set Mink Lash Extensions
Normally $208 Now $125
#Package 3- Eyebrow Threading plus Glossa Manicure Or Pedicure
Normally $128 Now $77
#Package 4- Eyebrow Threading plus Collagen Facial
Normally $148 Now $89
We would like to see designs that use pink with whit or black to suit logo & business name & final design should be girly/feminine 7 fun.
On the back we would like the following details:
Velvet Dawn Beauty, "Lindell Court", shop 7, 418 Marlowe Street, 3187
Tel: 03 9471 2360, Email: info@velvetdawnbeauty.example, Web: www.velvetdawnbeauty.example
A map of exact location and business hours:
Mon 9am to 5pm, Tue 9am to 6pm, Wed 9am to 6pm, Thu 9am to 8pm, Fri 9am to 6pm, sat 9am to 5pm

Target Market(s)

Women between the ages of 20 to 60 years of age

Industry/Entity Type

Hair

Font styles to use
Script

Colors
e34297
000000

Requirements
Must have
• Pink and black or pink and white colors
Should not have
• Fake looking eyelashes displayed

```html
<!DOCTYPE html>
<html lang="en">
<head>
<meta charset="utf-8">
<title>Velvet Dawn Beauty – Threading Combo Packages</title>
<link href="https://fonts.googleapis.com/css2?family=Arimo:wght@400;700&family=Oswald:wght@400;600&display=swap" rel="stylesheet">
<style>
  :root{
    --pink:#e34297;
    --black:#050505;
    --white:#ffffff;
    --stage:#3b3b42;
    --map-tone:#2a2a2c;
    --map-line:#dcdcdc;
    --photo-light:#d8b196;
    --photo-dark:#8a5a42;
  }
  *{box-sizing:border-box;margin:0;padding:0}
  html,body{width:1200px;height:1200px;overflow:hidden;background:var(--stage)}
  .stage{position:relative;width:1200px;height:1200px;display:flex;justify-content:center;align-items:center;gap:60px}
  .rack-card{position:relative;width:400px;height:880px;background:var(--black);color:var(--white);display:flex;flex-direction:column;box-shadow:0 20px 50px rgba(0,0,0,.45)}

  /* back */
  .back .contact{padding:44px 30px 24px;text-align:center;font-family:"Oswald",sans-serif;font-style:normal;font-size:17px;line-height:1.45;letter-spacing:.05em;text-transform:uppercase}
  .back .location-map{margin:0 34px;height:270px;background:var(--map-tone);border:6px solid var(--map-line);position:relative}
  .back .location-map svg{position:absolute;left:58%;top:58%;transform:translate(-50%,-50%)}
  .back .hours{margin-top:auto;height:340px;background:var(--pink);text-align:center;padding-top:42px;font-family:"Oswald",sans-serif}
  .brand-mark{display:flex;align-items:center;justify-content:center;gap:10px;font-family:"Arimo",sans-serif;font-weight:700;font-size:15px;letter-spacing:.14em;text-transform:uppercase;color:var(--white)}
  .brand-mark .dot{width:12px;height:12px;border-radius:50%;background:var(--white)}
  .hours h2{margin-top:34px;font-size:30px;font-weight:600;letter-spacing:.04em;text-transform:uppercase;color:var(--white)}
  .hours ul{list-style:none;margin-top:8px;font-size:18px;line-height:1.45;letter-spacing:.04em;text-transform:uppercase}

  /* front */
  .front .eye-photo{height:270px;background:linear-gradient(160deg,var(--photo-light) 0%,#c79577 55%,var(--photo-dark) 100%)}
  .front .offer{padding:24px 18px 0;text-align:center;font-family:"Arimo",sans-serif}
  .offer h1{font-size:34px;font-weight:400;color:var(--pink);text-transform:uppercase;white-space:nowrap;line-height:1}
  .offer .tagline{font-size:19px;margin-top:4px}
  .packages{list-style:none;margin-top:20px}
  .package{margin-bottom:18px}
  .package .name{font-size:14.5px;text-transform:uppercase;line-height:1.2;white-space:nowrap}
  .package .price{font-size:13px;margin-top:2px}
  .package .now{color:var(--pink);font-weight:700;font-size:15px}
  .front .brand-mark{margin-top:22px}
  .front .web-band{margin-top:auto;height:70px;background:var(--pink);display:flex;align-items:center;justify-content:center;font-family:"Arimo",sans-serif;font-weight:700;font-size:16px;letter-spacing:.04em;color:var(--black);text-transform:uppercase}
</style>
</head>
<body>
<main class="stage">
  <section class="rack-card back">
    <address class="contact">
      Lindell Court<br>
      Shop 7, 418 Marlowe Street, 3187<br>
      Tel: 03 9471 2360<br>
      info@velvetdawnbeauty.example<br>
      www.velvetdawnbeauty.example
    </address>
    <div class="location-map" role="img" aria-label="Street map showing the salon location">
      <svg width="30" height="40" viewBox="0 0 36 48" aria-hidden="true">
        <path d="M18 0C8 0 0 8 0 18c0 13 18 30 18 30s18-17 18-30C36 8 28 0 18 0z" fill="var(--pink)"/>
        <circle cx="18" cy="18" r="6" fill="var(--black)"/>
      </svg>
    </div>
    <div class="hours">
      <div class="brand-mark"><span class="dot"></span>Velvet Dawn Beauty</div>
      <h2>Store Hours</h2>
      <ul>
        <li>Mon: 9am to 5pm</li>
        <li>Tue &amp; Wed: 9am to 6pm</li>
        <li>Thu: 9am to 8pm</li>
        <li>Fri: 9am to 6pm</li>
        <li>Sat: 9am to 5pm</li>
      </ul>
    </div>
  </section>

  <section class="rack-card front">
    <div class="eye-photo" role="img" aria-label="Close-up photo of a shaped eyebrow and eye"></div>
    <div class="offer">
      <h1>Combo Packages</h1>
      <p class="tagline">Save 40% Off Original Price</p>
      <ul class="packages">
        <li class="package"><p class="name">Eyebrow Threading plus Eyebrow Tint<br>or Eyelash Tint</p><p class="price">Normally $53 <span class="now">Now $32</span></p></li>
        <li class="package"><p class="name">Eyebrow Threading plus Full Set Mink<br>Lash Extensions</p><p class="price">Normally $208 <span class="now">Now $125</span></p></li>
        <li class="package"><p class="name">Eyebrow Threading plus Glossa<br>Manicure or Pedicure</p><p class="price">Normally $128 <span class="now">Now $77</span></p></li>
        <li class="package"><p class="name">Eyebrow Threading plus Collagen Facial</p><p class="price">Normally $148 <span class="now">Now $89</span></p></li>
      </ul>
      <div class="brand-mark"><span class="dot"></span>Velvet Dawn Beauty</div>
    </div>
    <div class="web-band">velvetdawnbeauty.example</div>
  </section>
</main>
</body>
</html>
```